Update shopping site

Our current shopping website is outdated and we are wanting to update our shopping site to have a fresh new look/design.

Create a Web Design (Uncoded - PSD layout only)

We want you to develop the design for 4 pages:
1) Home Page
2) Remedy Type
3) Health Condition
4) Consultations

www.fernmoorwell.com

Reason: Close to choosing design and a few missing items to be resolved.

Industry/Entity Type

Shopping

```html
<!DOCTYPE html>
<html lang="en">
<head>
<meta charset="utf-8">
<title>Fernmoor Well – Home</title>
<link rel="stylesheet" href="https://fonts.googleapis.com/css2?family=Nunito+Sans:ital,wght@0,300;0,400;0,600;0,700;0,800&family=Open+Sans:ital,wght@1,300;1,400&display=swap">
<style>
:root{
  --green:#3fa33a;
  --green-dark:#2f8a2b;
  --orange:#d9762f;
  --teal:#3aa9c1;
  --ink:#222;
  --text:#444;
  --muted:#8a8a8a;
  --strike:#e08a4a;
  --line:#e3e3e3;
  --soft:#f5f5f5;
  --white:#fff;
}
*{margin:0;padding:0;box-sizing:border-box}
html,body{width:1200px;height:3000px;overflow:hidden;background:var(--white)}
body{font-family:"Nunito Sans",Arial,sans-serif;color:var(--text);position:relative}
.abs{position:absolute}
a{color:inherit;text-decoration:none}

/* header */
.site-header{position:absolute;left:0;top:0;width:1200px;height:124px;background:#fafafa}
.brand{position:absolute;left:100px;top:24px;display:flex;align-items:center;gap:18px}
.brand-mark{width:74px;height:74px;border-radius:50%;border:3px solid var(--green)}
.brand-name{color:var(--green-dark);font-weight:700;font-size:30px;line-height:36px}
.search{position:absolute;left:594px;top:22px;display:flex}
.search-field{width:240px;height:28px;border:1px solid #ccc;background:#fff;font-size:10px;color:#999;padding:7px 8px}
.search-btn{width:36px;height:28px;background:var(--green);display:flex;align-items:center;justify-content:center}
.util-links{position:absolute;left:892px;top:28px;display:flex;gap:24px;font-size:11px;color:var(--ink)}
.util-links .accent{color:var(--green)}
.account-links{position:absolute;right:100px;top:80px;display:flex;gap:40px;font-size:11px;color:var(--ink)}

.main-nav{position:absolute;left:0;top:124px;width:1200px;height:52px;background:var(--green);display:flex;justify-content:space-between;align-items:center;padding:0 116px;color:var(--white);font-size:15px}

/* hero */
.hero{position:absolute;left:0;top:176px;width:1200px;height:504px;background:linear-gradient(120deg,#6e8a4a 0%,#a9b98e 30%,#dfe3d6 55%,#8fa86a 75%,#4c6d2e 100%)}
.hero-title{position:absolute;left:0;top:86px;width:1200px;text-align:center;color:var(--white);font-weight:800;font-size:76px;letter-spacing:2px}
.hero-text{position:absolute;left:150px;top:186px;width:900px;text-align:center;color:var(--white);font-size:14px;line-height:24px}
.dots{position:absolute;left:556px;top:436px;display:flex;gap:10px}
.dot{width:14px;height:14px;border-radius:50%;background:var(--white)}
.dot.active{background:transparent;border:2px solid var(--white)}

/* welcome */
.section-title{position:absolute;left:0;width:1200px;text-align:center;color:var(--ink)}
.welcome-title{top:732px;font-size:36px;font-weight:300}
.welcome-text{position:absolute;left:120px;top:786px;width:960px;text-align:center;font-size:12px;line-height:24px;color:var(--ink)}
.service{position:absolute;top:896px;width:320px;text-align:center}
.service-icon{width:160px;height:160px;border-radius:50%;margin:0 auto;display:flex;align-items:center;justify-content:center;border:5px solid var(--white);box-shadow:0 0 0 3px currentColor}
.service h3{margin-top:16px;font-size:20px;font-weight:400;color:var(--ink)}
.service p{margin:10px auto 0;width:290px;font-size:14px;line-height:21px;color:var(--muted)}
.btn-outline{display:inline-block;margin-top:20px;width:152px;height:44px;line-height:40px;border:2px solid currentColor;font-size:16px}
.c-green{color:var(--green)} .c-orange{color:var(--orange)} .c-teal{color:var(--teal)}

/* featured */
.featured{position:absolute;left:0;top:1310px;width:1200px;height:738px;background:var(--soft)}
.featured-title{top:64px;font-size:34px;font-weight:700}
.featured-text{position:absolute;left:180px;top:130px;width:840px;text-align:center;font-size:14px;line-height:28px;color:var(--ink)}
.slider-arrows{position:absolute;left:1044px;top:184px;display:flex;gap:8px}
.slider-arrows span{width:24px;height:24px;border:1px solid #bbb;background:#fff;display:flex;align-items:center;justify-content:center}
.product{position:absolute;top:230px;width:220px;text-align:center}
.product-photo{width:220px;height:250px;border:1px solid var(--line);background:radial-gradient(ellipse 30% 60% at 50% 50%,var(--tone) 0%,#e6e2dc 60%,#fff 100%)}
.product-name{margin-top:20px;height:48px;font-size:15px;line-height:24px;color:var(--ink)}
.price{margin-top:10px;font-size:13px;color:var(--strike);display:flex;justify-content:center;gap:16px}
.price s{color:var(--strike)}
.btn-cart{display:inline-block;margin-top:22px;width:144px;height:40px;line-height:40px;background:var(--green);color:var(--white);font-weight:700;font-size:14px}

/* testimonials */
.testi-title{top:2098px;font-size:38px;font-weight:300}
.quote{position:absolute;left:190px;top:2186px;width:820px;text-align:center;font-family:"Open Sans",Arial,sans-serif;font-style:italic;font-weight:300;font-size:19px;line-height:29px;color:var(--text)}
.quote-mark{position:absolute;font-family:Georgia,serif;font-size:90px;color:#ddd;line-height:1}
.avatar{position:absolute;left:532px;top:2336px;width:136px;height:136px;border-radius:50%;border:6px solid #f0f0f0;background:radial-gradient(circle at 50% 40%,#e8d2b4,#b59a6c 70%,#8e8a5a)}
.client{top:2498px;font-size:16px;letter-spacing:2px;color:var(--ink)}
.side-arrow{position:absolute;top:2232px}

/* footer */
.site-footer{position:absolute;left:0;top:2606px;width:1200px;height:304px;background:var(--green);color:var(--white)}
.footer-col h4{font-size:20px;font-weight:700}
.footer-col{position:absolute;top:52px}
.footer-divider{position:absolute;top:52px;width:1px;height:200px;background:rgba(255,255,255,.3)}
.links{position:absolute;top:100px;font-size:14px;line-height:29px}
.contact-line{display:flex;gap:12px;align-items:center;font-size:14px;line-height:28px}
.newsletter{position:absolute;left:790px;top:104px;width:312px;height:44px;background:var(--white);border:2px solid var(--white);display:flex}
.newsletter-field{flex:1;color:#bbb;font-size:14px;padding:10px 12px;letter-spacing:1px}
.newsletter-btn{width:104px;background:var(--green);font-size:13px;font-weight:700;display:flex;align-items:center;justify-content:center}
.socials{position:absolute;left:790px;top:178px;display:flex;gap:12px}
.socials span{width:34px;height:34px;border-radius:50%;background:rgba(255,255,255,.25)}

.bottom-bar{position:absolute;left:0;top:2910px;width:1200px;height:90px;font-size:13px;color:var(--ink)}
.cards{position:absolute;left:940px;top:32px;display:flex;gap:10px;align-items:center}
.card-badge{width:36px;height:22px;border:1px solid #ccc;border-radius:3px;background:#f4f4f4}
</style>
</head>
<body>

<header class="site-header">
  <div class="brand">
    <div class="brand-mark"></div>
    <div class="brand-name">Welcome to Fernmoor Well<br>Nature for Life</div>
  </div>
  <div class="search">
    <div class="search-field">Search entire products here</div>
    <div class="search-btn">
      <svg width="14" height="14" viewBox="0 0 14 14"><circle cx="6" cy="6" r="4" fill="none" stroke="#fff" stroke-width="2"/><line x1="9" y1="9" x2="13" y2="13" stroke="#fff" stroke-width="2"/></svg>
    </div>
  </div>
  <nav class="util-links"><a class="accent">REGISTER</a><a>LOGIN</a><a>&#9632; MY CART(0)</a></nav>
  <nav class="account-links"><a>HOME</a><a>MY ACCOUNT</a><a>SHOPPING CART</a><a>CHECKOUT</a></nav>
</header>

<nav class="main-nav">
  <a>HOME</a><a>REMEDY TYPE</a><a>HEALTH CONDITION</a><a>ACCESSORIES &amp; SUPPLIES</a><a>LOYALTY PROGRAM</a><a>CONTACT US</a>
</nav>

<section class="hero" role="img" aria-label="Fresh medicinal herbs, a stone mortar and pestle, yellow flowers and glass oil bottles">
  <h1 class="hero-title">HEALTH CARE PRODUCTS</h1>
  <p class="hero-text">We offer some of the best botanical health care products in our industry (we require certificate of Analysis from our suppliers to ensure the purity of our product, that it is free of pesticides, contaminants, mold, fungus and it is the right product)</p>
  <div class="dots"><span class="dot active"></span><span class="dot"></span><span class="dot"></span><span class="dot"></span></div>
</section>

<h2 class="section-title welcome-title">WELCOME TO FERNMOOR WELL</h2>
<p class="welcome-text">We offer some of the best botanical health care products in our industry (we require certificate of Analysis from our suppliers to ensure the purity of our product, that it is free of pesticides, contaminants, mold, fungus and it is the right product); we have over 300 NPN (Natural Product Number) licenses approved by the Health Registry and our friendly staff is well qualified to answer most questions you may have. We also partner with professional practitioners if you require a more thorough consultation</p>

<div class="service c-green" style="left:80px">
  <div class="service-icon" style="background:var(--green)">
    <svg width="80" height="80" viewBox="0 0 80 80" fill="none" stroke="#fff" stroke-width="5" stroke-linejoin="round"><path d="M38 70 C18 60 10 40 14 18 C30 24 40 40 38 70Z"/><path d="M42 70 C62 60 70 40 66 18 C50 24 40 40 42 70Z"/></svg>
  </div>
  <h3>WILD CRAFTED HERBS</h3>
  <p>We prepare exceptional customized natural remedies for you and your family in most cases while you wait.</p>
  <a class="btn-outline">VIEW MORE</a>
</div>
<div class="service c-orange" style="left:440px">
  <div class="service-icon" style="background:var(--orange)">
    <svg width="90" height="70" viewBox="0 0 90 70" fill="none" stroke="#fff" stroke-width="4"><path d="M14 30 H66 V40 C66 54 54 62 40 62 C26 62 14 54 14 40Z" fill="#fff"/><path d="M66 34 C80 34 80 50 64 50"/><path d="M6 66 H74"/><circle cx="40" cy="16" r="8"/></svg>
  </div>
  <h3>MEDICINAL TEAS</h3>
  <p>We prepare exceptional customized natural remedies for you and your family in most cases while you wait.</p>
  <a class="btn-outline">VIEW MORE</a>
</div>
<div class="service c-teal" style="left:800px">
  <div class="service-icon" style="background:var(--teal)">
    <svg width="60" height="84" viewBox="0 0 60 84"><rect x="20" y="2" width="20" height="10" fill="#fff"/><rect x="6" y="16" width="48" height="66" rx="6" fill="#fff"/><path d="M30 34 V64 M15 49 H45" stroke="var(--teal)" stroke-width="8"/></svg>
  </div>
  <h3>HEALING CREAMS AND SALVES</h3>
  <p>We prepare exceptional customized natural remedies for you and your family in most cases while you wait.</p>
  <a class="btn-outline">VIEW MORE</a>
</div>

<section class="featured">
  <h2 class="section-title featured-title">FEATURED PRODUCTS</h2>
  <p class="featured-text">Sed ut perspiciatis unde omnis iste natus error sit voluptatem accusantium doloremque laudantium, totam rem aperiam, eaque ipsa quae ab illo inventore veritatis et quasi architecto beatae vitae dicta sunt explicabo</p>
  <div class="slider-arrows">
    <span><svg width="8" height="10"><path d="M6 1 L2 5 L6 9" stroke="#888" fill="none"/></svg></span>
    <span><svg width="8" height="10"><path d="M2 1 L6 5 L2 9" stroke="#888" fill="none"/></svg></span>
  </div>

  <div class="product" style="left:100px">
    <div class="product-photo" role="img" aria-label="Product photo: amber dropper bottle of goat's rue tincture" style="--tone:#6b3a24"></div>
    <p class="product-name">Goat's Rue - Extract (Tincture)<br>(Galega officinalis )</p>
    <p class="price"><s>$13.99-$45.99</s><span>$5.99-$43.99</span></p>
    <a class="btn-cart">ADD TO CART</a>
  </div>
  <div class="product" style="left:360px">
    <div class="product-photo" role="img" aria-label="Product photo: small bottle of lavender essential oil" style="--tone:#7a5a40"></div>
    <p class="product-name">Lavender (French) - Essential<br>Oil (Lavandula angustifolia)</p>
    <p class="price"><s>$20.99-$30.99</s><span>$7.99-$14.99</span></p>
    <a class="btn-cart">ADD TO CART</a>
  </div>
  <div class="product" style="left:620px">
    <div class="product-photo" role="img" aria-label="Product photo: dropper bottle of chasteberry extract" style="--tone:#4a6a3a"></div>
    <p class="product-name">Chasteberry / Vitex - Extract<br>(Tincture) (Vitex agnus-castus )</p>
    <p class="price"><s>$19.99</s><span>$16.99</span></p>
    <a class="btn-cart">ADD TO CART</a>
  </div>
  <div class="product" style="left:880px">
    <div class="product-photo" role="img" aria-label="Product photo: dropper bottle of damiana extract" style="--tone:#6a5422"></div>
    <p class="product-name">Damiana - Extract (Tincture)<br>(Turnera diffusa )</p>
    <p class="price"><s>$105.00</s><span>$35.00</span></p>
    <a class="btn-cart">ADD TO CART</a>
  </div>
</section>

<h2 class="section-title testi-title">Client Testimonials</h2>
<svg class="side-arrow" style="left:98px" width="14" height="26"><path d="M12 2 L2 13 L12 24" stroke="#ccc" stroke-width="2" fill="none"/></svg>
<svg class="side-arrow" style="left:1086px" width="14" height="26"><path d="M2 2 L12 13 L2 24" stroke="#ccc" stroke-width="2" fill="none"/></svg>
<span class="quote-mark" style="left:140px;top:2170px">&ldquo;</span>
<p class="quote">But I must explain to you how all this mistaken idea of denouncing pleasure and praising pain was born and I will give you a complete account of the system, and expound the actual teachings of the great explorer of the truth, the master-builder of human happiness. No one rejects, dislikes, or avoids pleasure itself, because it is pleasure, but because those who do not know how to pursue pleasure rationally encounter consequences that are extremely painful</p>
<span class="quote-mark" style="left:1004px;top:2290px">&rdquo;</span>
<div class="avatar" role="img" aria-label="Portrait photo of the client"></div>
<p class="section-title client">- ASSUMENDA EST</p>

<footer class="site-footer">
  <div class="footer-col" style="left:100px"><h4>Information</h4></div>
  <div class="links" style="left:100px"><a>About Us</a><br><a>Loyalty Program</a><br><a>Shipping Information</a><br><a>Consultation</a><br><a>Privacy Policy</a></div>
  <div class="links" style="left:278px"><a>Terms &amp; Conditions</a><br><a>Video</a><br><a>Community Links</a><br><a>Health Info</a><br><a>Returns Policy</a></div>
  <div class="footer-divider" style="left:432px"></div>
  <div class="footer-col" style="left:460px"><h4>Contact Us</h4></div>
  <div class="links" style="left:460px;width:300px;line-height:26px">
    <p style="font-size:13px">Fernmoor Well Herbal Dispensary 418<br>Alder Row, Vancouver, B.C. Canada V5X 1R7</p>
    <p class="contact-line" style="margin-top:10px"><svg width="16" height="16" viewBox="0 0 16 16"><path d="M3 1 L6 1 L7 5 L5 6.5 C6 9 7 10 9.5 11 L11 9 L15 10 L15 13 C15 14 14 15 13 15 C6 15 1 10 1 3 C1 2 2 1 3 1Z" fill="#fff"/></svg>604.555.0187</p>
    <p class="contact-line"><svg width="16" height="12" viewBox="0 0 16 12"><rect width="16" height="12" rx="1" fill="#fff"/><path d="M1 1 L8 7 L15 1" stroke="var(--green)" stroke-width="1.5" fill="none"/></svg>info@fernmoorwell.com</p>
  </div>
  <div class="footer-divider" style="left:762px"></div>
  <div class="footer-col" style="left:790px"><h4>Join Newsletters</h4></div>
  <div class="newsletter"><div class="newsletter-field">EMAIL ADDRESS</div><div class="newsletter-btn">SUBSCRIBE</div></div>
  <div class="socials"><span></span><span></span><span></span><span></span><span></span></div>
</footer>

<div class="bottom-bar">
  <p class="abs" style="left:100px;top:34px">© 2017 Fernmoor Well Herbal Dispensary .&nbsp; All right reserved.&nbsp; Term of Use</p>
  <div class="cards">
    <span style="margin-right:8px">We Accept:</span>
    <span class="card-badge"></span><span class="card-badge"></span><span class="card-badge"></span><span class="card-badge"></span>
  </div>
</div>

</body>
</html>
```